Website for peer to peer car sharing service

Hi all,

We need a web design for a new environmental friendly peer-to-peer car sharing website.

The website will serve as a marketplace where car owners can list their car and drivers that who do not have access to a car can rent a suitable car. It is important for us to emphasis that this is a community where the main purpose is to use the vehicles on the street in a more efficient way.

Attached are five pictures where we have sketched up the five main pages:

File 1. Info site for a particular car.
File 2. Logo.
File 3. Register a car.
File 4. Sign up.
File 5. Search.
File 6. Front page.

The logo for the company is attached (File 2) and it would be ideal to design the website in relation to the logo. The final design should relate to a secure market place which is environmental friendly.

We would like this webpage to be in the same spirit as www.velnoro.it, www.brundale.com, www.plimtrovesite.com, https://wend.kul.net, https://garbelow.com etc.

We look forward to see your designs.

Best regards,
The Trundo Team.

Hi guys, 

Please take :

1) Could you please design icons for for  'FAQ' and 'Insurance' in the header, locate the icons right to the Trundo logo. We only want two icons ('FAQ' and 'Insurance')  right to the Trundo logo.

2) The height of the header should be the same as the header of faplex.com

3) The price tags for the cars (below the top section) should be similar to the price tags at mostanbee.com.

4) We would like you to start to design the other pages (the sub-pages listed in the project description:
a)Info site for a particular car.
b)Register a car. 
c)Search results (similar to http://www.pevrotank.com/find-car).

Please take a look at the picture attached for the sub-pages:

https://files.quenmolt.example/brief_uploads/000001_3_search_000001_brief000001.jpg

https://files.quenmolt.example/brief_uploads/000002_4_infositeforaparticularcar_000002_brief000002.jpg

http://www.quenmolt.example/file.aspx?fileLocation=storage_url/brief_uploads/000003_5_registeracar_brief000003.jpg

Best regards, 
Trundo team 

Target Market(s)

The target market are people from 20-40 years old who are environmental friendly, also tourists who visit the city and would like to rent a car.

Industry/Entity Type

It Company

Requirements
Must have
• It is required that the designer that will be chosen will hand in layered PSD files of each web page.

```html
<!DOCTYPE html>
<html lang="en">
<head>
<meta charset="utf-8">
<title>Trundo – Peer to peer car sharing</title>
<link href="https://fonts.googleapis.com/css2?family=Bebas+Neue&family=Open+Sans:wght@400;600;700&display=swap" rel="stylesheet">
<style>
:root{
  --ink:#2b2d30;
  --text:#55595e;
  --muted:#8a8f94;
  --green:#8cc63f;
  --green-dark:#6fa52a;
  --red:#e0342a;
  --orange:#f7931e;
  --page:#e9eef2;
  --band:#dce1e5;
  --strip:#e8edf1;
  --footer:#2f3033;
  --footer-text:#a4a8ad;
  --rule:#cfd4d8;
  --hex:#c7ccd0;
  --white:#ffffff;
}
*{box-sizing:border-box;margin:0;padding:0}
html,body{width:1200px;height:2526px;overflow:hidden}
body{position:relative;background:var(--page);font-family:"Open Sans",Arial,sans-serif;color:var(--text)}
.abs{position:absolute}

/* header */
.topbar{position:absolute;left:0;top:0;width:1200px;height:34px;background:rgba(0,0,0,.82);z-index:3}
.brand{position:absolute;left:130px;top:4px;display:flex;align-items:center;gap:7px;color:var(--white);font-weight:700;font-size:20px;line-height:26px}
.brand-dot{width:14px;height:14px;border-radius:50%;background:var(--green)}
.btn-list{position:absolute;left:722px;top:6px;width:107px;height:22px;background:var(--green);color:#1d2a0c;font-size:10.5px;font-weight:600;text-align:center;line-height:22px}
.nav-link{position:absolute;top:6px;color:var(--white);font-size:11px;line-height:22px}
.nav-sep{position:absolute;left:908px;top:6px;color:#888;font-size:11px;line-height:22px}
.nav-icon{position:absolute;top:4px}

/* hero */
.hero{position:absolute;left:0;top:0;width:1200px;height:568px;background:linear-gradient(180deg,#5b6470 0%,#7c8690 35%,#3c434b 70%,#9aa3ab 100%)}
.hero-title{position:absolute;left:0;width:1200px;top:118px;text-align:center;font-family:"Bebas Neue",Impact,sans-serif;color:var(--white);font-size:80px;line-height:80px;letter-spacing:1px}
.hero-sub{position:absolute;left:0;width:1200px;top:198px;text-align:center;font-family:"Bebas Neue",Impact,sans-serif;color:var(--white);font-size:42px;line-height:42px}
.search-box{position:absolute;left:375px;top:307px;width:450px;height:76px;background:rgba(0,0,0,.75)}
.search-input{position:absolute;left:19px;top:15px;width:288px;height:42px;background:var(--white);border-radius:3px;color:#666;font-size:14px;line-height:42px;padding-left:12px}
.search-btn{position:absolute;left:322px;top:15px;width:110px;height:42px;background:var(--green);border-radius:3px;color:#1d2a0c;font-weight:600;font-size:14px;line-height:42px;text-align:center}
.promo{position:absolute;left:130px;top:467px;width:137px;height:116px;background:var(--orange);color:var(--white);text-align:center;z-index:2}
.promo-amount{font-weight:700;font-size:42px;line-height:46px;margin-top:18px}
.promo-amount small{font-size:20px;vertical-align:middle}
.promo-note{font-size:13px}

/* car cards */
.car-card{position:absolute;top:606px;width:283px;height:320px;background:var(--white);box-shadow:0 1px 3px rgba(0,0,0,.12)}
.car-photo{position:absolute;left:13px;top:13px;width:257px;height:152px}
.car-name{position:absolute;left:15px;top:174px;font-weight:700;font-size:14px;color:var(--ink)}
.car-price{position:absolute;right:15px;top:174px;font-weight:700;font-size:14px;color:var(--red)}
.car-desc{position:absolute;left:15px;top:198px;width:250px;font-size:11px;line-height:16px}
.owner-photo{position:absolute;left:23px;top:244px;width:44px;height:52px;background:linear-gradient(#c7b39e,#8a7563)}
.owner-name{position:absolute;left:98px;top:242px;font-weight:600;font-size:11px;color:var(--ink)}
.owner-pin{position:absolute;left:77px;top:262px}
.owner-addr{position:absolute;left:98px;top:260px;font-size:11px;line-height:17px}

/* section headings */
.section-title{position:absolute;font-weight:700;font-size:22px;color:var(--ink);line-height:28px}
.section-rule{position:absolute;height:6px;background:var(--rule)}

/* posts */
.post-title{position:absolute;left:130px;font-weight:700;font-size:13px;color:var(--ink)}
.post-date{position:absolute;left:130px;font-size:9.5px;color:var(--muted)}
.post-body{position:absolute;left:130px;width:600px;font-size:12px;line-height:23px}
.post-more{position:absolute;left:130px;font-weight:600;font-size:10.5px;color:var(--ink)}
.post-sep{position:absolute;left:130px;width:611px;height:1px;background:var(--rule)}

.video{position:absolute;left:787px;top:1036px;width:283px;height:217px;background:linear-gradient(160deg,#5a4a3a,#8e3a2c 55%,#3d3a36)}
.play{position:absolute;left:116px;top:83px}

/* insurance band */
.band{position:absolute;left:0;top:1320px;width:1200px;height:705px;background:var(--band)}
.insure-art{position:absolute;left:130px;top:1347px;width:407px;height:221px;background:radial-gradient(ellipse at 50% 50%,#d9dcdf,#9ea3a8 70%,var(--band) 72%)}
.insure-title{position:absolute;left:558px;top:1380px;font-weight:700;font-size:20px;color:var(--ink)}
.insure-text{position:absolute;left:558px;width:505px;font-size:11.5px;line-height:21px}

.social-box{position:absolute;left:787px;top:1737px;width:283px;height:217px;background:var(--white);border:1px solid #c9ced2}
.social-head{position:absolute;left:8px;top:8px;width:44px;height:44px;background:#2b2d30}
.social-name{position:absolute;left:60px;top:6px;font-size:12px;color:#3b5998;font-weight:600}
.social-on{font-size:9px;font-weight:400;color:var(--muted)}
.social-like{position:absolute;left:60px;top:26px;width:42px;height:18px;border:1px solid #c9ced2;background:#f1f2f4;font-size:10px;text-align:center;line-height:16px;color:#444}
.social-signup{position:absolute;right:14px;top:24px;width:56px;height:22px;background:var(--green);color:var(--white);font-size:11px;font-weight:600;line-height:22px;text-align:center}
.social-count{position:absolute;left:8px;top:64px;font-size:10px;color:#444}
.social-fans{position:absolute;left:8px;top:82px;width:265px;height:100px;background:linear-gradient(90deg,#9c8a7c,#c8b3a2,#7d6a5f,#b6a090)}
.social-foot{position:absolute;left:8px;top:194px;font-size:9px;color:var(--muted)}

/* press strip */
.press{position:absolute;left:0;top:2025px;width:1200px;height:219px;background:var(--strip)}
.press-item{position:absolute;top:2054px;width:138px;height:158px}
.press-label{position:absolute;left:0;top:54px;width:138px;text-align:center;font-size:15px;line-height:20px;color:#6b7075}

/* footer */
.footer{position:absolute;left:0;top:2244px;width:1200px;height:282px;background:var(--footer)}
.foot-title{position:absolute;font-weight:700;font-size:12px;color:var(--white)}
.foot-text{position:absolute;font-size:11px;line-height:18px;color:var(--footer-text)}
.foot-brand{position:absolute;left:895px;top:2478px;display:flex;align-items:center;gap:7px;color:var(--white);font-weight:700;font-size:22px}
</style>
</head>
<body>

<section class="hero" role="img" aria-label="Sports car photographed in a modern glass hall"></section>

<header class="topbar">
  <div class="brand"><span class="brand-dot"></span>Trundo</div>
  <div class="btn-list">LIST YOUR CAR</div>
  <div class="nav-link" style="left:853px">LOGIN</div>
  <div class="nav-sep">|</div>
  <div class="nav-link" style="left:933px">SING UP</div>
  <svg class="nav-icon" style="left:1008px" width="22" height="26" viewBox="0 0 22 26" aria-label="FAQ">
    <path d="M5 8a6 6 0 1 1 9 5c-2 1-3 2-3 4v1" fill="none" stroke="#fff" stroke-width="3"/>
    <circle cx="11" cy="23" r="2" fill="#fff"/>
  </svg>
  <svg class="nav-icon" style="left:1040px" width="26" height="26" viewBox="0 0 26 26" aria-label="Insurance">
    <circle cx="13" cy="13" r="11" fill="none" stroke="#fff" stroke-width="2"/>
    <rect x="7" y="10" width="12" height="6" rx="2" fill="#fff"/>
    <circle cx="9" cy="18" r="1.6" fill="#fff"/><circle cx="17" cy="18" r="1.6" fill="#fff"/>
  </svg>
</header>

<h1 class="hero-title">LOREM IPSUM IS SIMPLY TEXT</h1>
<p class="hero-sub">SUBTITLE GOES HERE</p>
<form class="search-box">
  <div class="search-input">Type here...</div>
  <div class="search-btn">FIND CAR</div>
</form>
<div class="promo">
  <div class="promo-amount">$10 <small>off</small></div>
  <div class="promo-note">your first rental</div>
</div>

<!-- car listings -->
<article class="car-card" style="left:130px">
  <div class="car-photo" role="img" aria-label="Black sports car" style="background:linear-gradient(180deg,#5d5f63,#1d1e21 70%,#3a3b3e)"></div>
  <div class="car-name">Car Name</div><div class="car-price">$ 556.05</div>
  <p class="car-desc">Lorem Ipsum is simply dummy text of the print-ing and typesetting industry.</p>
  <div class="owner-photo" role="img" aria-label="Owner portrait"></div>
  <div class="owner-name">Owner's Name</div>
  <svg class="owner-pin" width="14" height="20" viewBox="0 0 14 20"><path d="M7 0a7 7 0 0 1 7 7c0 5-7 13-7 13S0 12 0 7a7 7 0 0 1 7-7z" fill="#b9bdc1"/><circle cx="7" cy="7" r="2.6" fill="#fff"/></svg>
  <p class="owner-addr">256, Lorem ipsum amet dolor,<br>kamnsuhue, lonala-358686</p>
</article>
<article class="car-card" style="left:461px">
  <div class="car-photo" role="img" aria-label="Silver sports car" style="background:linear-gradient(180deg,#7a6a55,#c9ccd0 50%,#5e5a55)"></div>
  <div class="car-name">Car Name</div><div class="car-price">$ 556.05</div>
  <p class="car-desc">Lorem Ipsum is simply dummy text of the print-ing and typesetting industry.</p>
  <div class="owner-photo" role="img" aria-label="Owner portrait"></div>
  <div class="owner-name">Owner's Name</div>
  <svg class="owner-pin" width="14" height="20" viewBox="0 0 14 20"><path d="M7 0a7 7 0 0 1 7 7c0 5-7 13-7 13S0 12 0 7a7 7 0 0 1 7-7z" fill="#b9bdc1"/><circle cx="7" cy="7" r="2.6" fill="#fff"/></svg>
  <p class="owner-addr">256, Lorem ipsum amet dolor,<br>kamnsuhue, lonala-358686</p>
</article>
<article class="car-card" style="left:789px">
  <div class="car-photo" role="img" aria-label="Copper sports car on a road" style="background:linear-gradient(180deg,#8fb0d4,#b57a4a 55%,#7d7b6f)"></div>
  <div class="car-name">Car Name</div><div class="car-price">$ 556.05</div>
  <p class="car-desc">Lorem Ipsum is simply dummy text of the print-ing and typesetting industry.</p>
  <div class="owner-photo" role="img" aria-label="Owner portrait"></div>
  <div class="owner-name">Owner's Name</div>
  <svg class="owner-pin" width="14" height="20" viewBox="0 0 14 20"><path d="M7 0a7 7 0 0 1 7 7c0 5-7 13-7 13S0 12 0 7a7 7 0 0 1 7-7z" fill="#b9bdc1"/><circle cx="7" cy="7" r="2.6" fill="#fff"/></svg>
  <p class="owner-addr">256, Lorem ipsum amet dolor,<br>kamnsuhue, lonala-358686</p>
</article>

<!-- latest news -->
<h2 class="section-title" style="left:130px;top:970px">LATEST NEWS</h2>
<div class="section-rule" style="left:130px;top:1011px;width:611px"></div>
<h2 class="section-title" style="left:787px;top:970px">VIDEO</h2>
<div class="section-rule" style="left:787px;top:1011px;width:283px"></div>

<h3 class="post-title" style="top:1033px">Lorem Ipsum is simply dummy text of the printing and typesetting industry.</h3>
<p class="post-date" style="top:1056px">Posted on 18th February, 2013</p>
<p class="post-body" style="top:1075px">Lorem Ipsum is simply dummy text of the printing and typesetting industry. Lorem Ipsum has been the Industry's standard dummy when an unknown printer took a make a type specimen book.</p>
<p class="post-more" style="top:1124px">Learn More &gt;&gt;</p>
<div class="post-sep" style="top:1157px"></div>
<h3 class="post-title" style="top:1170px">Lorem Ipsum is simply dummy text of the printing and typesetting industry.</h3>
<p class="post-date" style="top:1193px">Posted on 18th February, 2013</p>
<p class="post-body" style="top:1212px">Lorem Ipsum is simply dummy text of the printing and typesetting industry. Lorem Ipsum has been the Industry's standard dummy when an unknown printer took a make a type specimen book.</p>
<p class="post-more" style="top:1261px">Learn More &gt;&gt;</p>

<div class="video" role="img" aria-label="Video still of a red car on a mountain road">
  <svg class="play" width="52" height="52" viewBox="0 0 52 52"><circle cx="26" cy="26" r="23" fill="none" stroke="#fff" stroke-width="3"/><path d="M21 16l15 10-15 10z" fill="#fff"/></svg>
</div>

<!-- insurance and blog band -->
<section class="band"></section>
<div class="insure-art" role="img" aria-label="Car wrapped in protective foil"></div>
<h2 class="insure-title">Your Car is Fully Covered with insurances</h2>
<p class="insure-text" style="top:1412px">Lorem Ipsum is simply dummy text of the printing and typesetting industry. Lorem Ipsum has been the industry's standard dummy when an unknown printer took a make a type specimen book Lorem Ipsum is simply dummy text of the printing and typesetting industry. Lorem Ipsum has been the industry's standard dummy when an unknown printer took a make a type specimen book</p>
<p class="insure-text" style="top:1533px">Lorem Ipsum is simply dummy text of the printing and typesetting industry. Lorem Ipsum has been the industry's standard dummy when an unknown printer took a make a type specimen book</p>

<h2 class="section-title" style="left:130px;top:1670px">LATEST BLOG</h2>
<div class="section-rule" style="left:130px;top:1711px;width:611px"></div>
<h2 class="section-title" style="left:787px;top:1670px">PLAZANET</h2>
<div class="section-rule" style="left:787px;top:1711px;width:283px"></div>

<h3 class="post-title" style="top:1733px">Lorem Ipsum is simply dummy text of the printing and typesetting industry.</h3>
<p class="post-date" style="top:1756px">Posted on 18th February, 2013 | Comments (0)</p>
<p class="post-body" style="top:1775px">Lorem Ipsum is simply dummy text of the printing and typesetting industry. Lorem Ipsum has been the Industry's standard dummy when an unknown printer took a make a type specimen book.</p>
<p class="post-more" style="top:1824px">Learn More &gt;&gt;</p>
<div class="post-sep" style="top:1857px"></div>
<h3 class="post-title" style="top:1870px">Lorem Ipsum is simply dummy text of the printing and typesetting industry.</h3>
<p class="post-date" style="top:1893px">Posted on 18th February, 2013 | Comments (0)</p>
<p class="post-body" style="top:1912px">Lorem Ipsum is simply dummy text of the printing and typesetting industry. Lorem Ipsum has been the Industry's standard dummy when an unknown printer took a make a type specimen book.</p>
<p class="post-more" style="top:1961px">Learn More &gt;&gt;</p>

<aside class="social-box">
  <div class="social-head"></div>
  <div class="social-name">Trundo <span class="social-on">on Plazanet</span></div>
  <div class="social-like">Like</div>
  <div class="social-signup">Sign Up</div>
  <div class="social-count">560 people like Trundo</div>
  <div class="social-fans" role="img" aria-label="Grid of member pictures"></div>
  <div class="social-foot">Plazanet social plugin</div>
</aside>

<!-- press -->
<section class="press"></section>
<div class="press-item" style="left:211px">
  <svg width="138" height="158" viewBox="0 0 138 158"><polygon points="69,0 138,39 138,119 69,158 0,119 0,39" fill="#c7ccd0"/></svg>
  <div class="press-label">NEWS PAPER<br>LOGO HERE</div>
</div>
<div class="press-item" style="left:426px">
  <svg width="138" height="158" viewBox="0 0 138 158"><polygon points="69,0 138,39 138,119 69,158 0,119 0,39" fill="#c7ccd0"/></svg>
  <div class="press-label">NEWS PAPER<br>LOGO HERE</div>
</div>
<div class="press-item" style="left:640px">
  <svg width="138" height="158" viewBox="0 0 138 158"><polygon points="69,0 138,39 138,119 69,158 0,119 0,39" fill="#c7ccd0"/></svg>
  <div class="press-label">NEWS PAPER<br>LOGO HERE</div>
</div>
<div class="press-item" style="left:855px">
  <svg width="138" height="158" viewBox="0 0 138 158"><polygon points="69,0 138,39 138,119 69,158 0,119 0,39" fill="#c7ccd0"/></svg>
  <div class="press-label">NEWS PAPER<br>LOGO HERE</div>
</div>

<!-- footer -->
<footer class="footer"></footer>
<div class="foot-title" style="left:130px;top:2280px">QUICK LINKS</div>
<div class="foot-text" style="left:130px;top:2308px">Info site for a particular car &nbsp;|&nbsp; Register a car &nbsp;|&nbsp; Search results &nbsp;|&nbsp; FAQ &nbsp;|&nbsp; Insurance</div>

<svg class="abs" style="left:861px;top:2278px" width="18" height="26" viewBox="0 0 14 20"><path d="M7 0a7 7 0 0 1 7 7c0 5-7 13-7 13S0 12 0 7a7 7 0 0 1 7-7z" fill="#8a8e93"/><circle cx="7" cy="7" r="2.6" fill="#2f3033"/></svg>
<div class="foot-title" style="left:895px;top:2280px">LOCATION</div>
<div class="foot-text" style="left:895px;top:2310px">256, Lorem ipsum amet dolor,<br>kamnsuhue, lonala-358686</div>

<svg class="abs" style="left:859px;top:2377px" width="24" height="18" viewBox="0 0 24 18"><rect x="1" y="1" width="22" height="16" fill="#8a8e93"/><path d="M1 1l11 9 11-9" fill="none" stroke="#2f3033" stroke-width="2"/></svg>
<div class="foot-title" style="left:895px;top:2376px">CONTACT INFO</div>
<div class="foot-text" style="left:895px;top:2404px">Phone : (900) 40 417 2063<br>Email : info@trundomail.example</div>

<div class="foot-text" style="left:130px;top:2488px">Copyright ©2013 Trundo. All Rights Reserved.</div>
<div class="foot-brand"><span class="brand-dot"></span>Trundo</div>

</body>
</html>
```